Header for Academic Handouts (How-to-Guides)

We are looking for a design element, which can be used as a visual header on A4-word-documents (Portrait-Set-Up). It shall be a graphic, visual language which is clearly understandable. The header height shall be between 0.75 - 1.5 inch – so it should not have too many small details. Attached below ideas/directions how the final document could look like.

The visual element shall symbolize by simple means the topic of “flipped classroom” or “active learning”. The documents with these new graphic elements will be used on handouts which are distributed in this training course:
https://www.korvanel.ch/en/the-korvanel-academy/education/educational-development/didaktische-weiterbildung/flipped-classroom.html

```html
<!DOCTYPE html>
<html lang="en">
<head>
<meta charset="utf-8">
<title>Flipped Classroom – Teaching Lab Handout Header</title>
<link rel="stylesheet" href="https://fonts.googleapis.com/css2?family=Roboto+Condensed:ital,wght@0,700;1,700&family=Titillium+Web:wght@600&display=swap">
<style>
  :root {
    --stage: #e4e4e4;
    --paper: #ffffff;
    --orange: #ff9900;
    --gold: #ebbf40;
    --rule: #f0b73a;
    --on-band: #ffffff;
  }
  html, body {
    margin: 0;
    padding: 0;
    width: 1200px;
    height: 1200px;
    overflow: hidden;
    background: var(--stage);
  }
  .canvas {
    width: 1200px;
    height: 1200px;
    display: flex;
    align-items: center;
    justify-content: center;
  }
  .handout {
    display: block;
    width: 827px;
    height: 1160px;
    background: var(--paper);
  }
  .band-orange { fill: var(--orange); }
  .band-gold { fill: var(--gold); }
  .rule { fill: var(--rule); }
  .title-topic {
    font-family: "Roboto Condensed", "Arial Narrow", sans-serif;
    font-weight: 700;
    font-style: italic;
    font-size: 54px;
    fill: var(--on-band);
  }
  .title-lab {
    font-family: "Roboto Condensed", "Arial Narrow", sans-serif;
    font-weight: 700;
    font-size: 52px;
    fill: var(--on-band);
  }
  .footer-info {
    font-family: "Titillium Web", Arial, sans-serif;
    font-weight: 600;
    font-size: 21px;
    fill: var(--on-band);
  }
  .footer-brand {
    font-family: "Titillium Web", Arial, sans-serif;
    font-weight: 600;
    font-size: 48px;
    fill: var(--on-band);
  }
</style>
</head>
<body>
  <main class="canvas">
    <svg class="handout" viewBox="0 0 917 1286" xmlns="http://www.w3.org/2000/svg" aria-label="Flipped Classroom Teaching Lab handout template">
      <g class="header">
        <polygon class="band-orange" points="0,76 553,76 474,207 0,207"/>
        <polygon class="band-gold" points="585,40 917,40 917,207 484,207"/>
        <rect class="rule" x="0" y="219" width="917" height="4"/>
        <text class="title-topic" x="69" y="153" textLength="388" lengthAdjust="spacingAndGlyphs">Flipped Classroom</text>
        <text class="title-lab" x="579" y="153" textLength="274" lengthAdjust="spacingAndGlyphs">Teaching Lab</text>
      </g>
      <g class="footer">
        <rect class="rule" x="0" y="1167" width="917" height="4"/>
        <rect class="band-gold" x="0" y="1176" width="917" height="110"/>
        <text class="footer-info" x="65" y="1219" textLength="375" lengthAdjust="spacingAndGlyphs">Centre for Learning Design and Practice</text>
        <text class="footer-info" x="65" y="1245">www.cldp.korvanel.ch</text>
        <text class="footer-brand" x="826" y="1242" text-anchor="end">Korvanel</text>
      </g>
    </svg>
  </main>
</body>
</html>
```